Stationery modern simple design
Corporate Stationery
Project: Stationery modern simple design
Creative Brief
Simple
Faisal Alqurashi
General Manager
Sable Grid Company 3858 Nakheel Crest Rd Wardah Tower Riyadh 13847 Saudi Arabia
info@sablegrid.example
www.sablegrid.example
address will be not use in business card and will be used in any other Stationery Arabic Address: شركة سابل جريد ٣٨٥٨ طريق النخيل الأعلى الرياض ١٣٨٤٧ المملكة العربية السعودية
فيصل القرشي المدير العام infor@sablegrid.example +966117290813 +9665031476095

```html
<!DOCTYPE html>
<html lang="en">
<head>
<meta charset="utf-8">
<title>Sable Grid – Business Card</title>
<link href="https://fonts.googleapis.com/css2?family=Montserrat:wght@400;600;700&family=Open+Sans:wght@400;600&family=Noto+Kufi+Arabic:wght@400&display=swap" rel="stylesheet">
<style>
  :root {
    --stage: #2b2d31;
    --card-white: #ffffff;
    --brand-blue: #1a8fdc;
    --brand-blue-deep: #0b66b8;
    --brand-blue-light: #35b0f0;
    --ink-grey: #5d6168;
    --ink-dark: #3a3d42;
    --rule: #c9ccd1;
  }
  * { box-sizing: border-box; margin: 0; padding: 0; }
  html, body {
    width: 1200px; height: 901px; overflow: hidden;
    background: var(--stage);
  }
  .stage {
    width: 1200px; height: 901px;
    display: flex; align-items: center; justify-content: center; gap: 60px;
  }
  .card {
    width: 525px; height: 300px; position: relative; overflow: hidden;
    box-shadow: 0 18px 40px rgba(0,0,0,.45);
  }
  /* Front */
  .card-front { background: var(--card-white); display: flex; align-items: center; }
  .brand-block {
    width: 250px; display: flex; align-items: center; justify-content: center; gap: 10px;
  }
  .brand-dot { width: 14px; height: 14px; background: var(--brand-blue); }
  .brand-name {
    font-family: "Montserrat", sans-serif; font-weight: 600; font-size: 26px;
    letter-spacing: 1px; color: var(--brand-blue);
  }
  .divider { width: 1px; height: 150px; background: var(--rule); }
  .contact-block { padding-left: 24px; font-family: "Open Sans", sans-serif; }
  .person-name {
    font-family: "Montserrat", sans-serif; font-weight: 700; font-size: 16px;
    color: var(--brand-blue); text-transform: uppercase; letter-spacing: .5px;
  }
  .person-title { font-size: 12px; color: var(--ink-grey); margin-bottom: 14px; }
  .contact-list { list-style: none; }
  .contact-list li {
    display: flex; align-items: center; gap: 8px;
    font-size: 11.5px; color: var(--ink-dark); line-height: 20px;
  }
  .contact-icon { width: 13px; height: 13px; flex: none; }
  /* Back */
  .card-back {
    background: linear-gradient(135deg, var(--brand-blue-light) 0%, var(--brand-blue) 45%, var(--brand-blue-deep) 100%);
  }
  .back-mark {
    position: absolute; right: 34px; bottom: 44px; text-align: right; color: #fff;
  }
  .back-name {
    font-family: "Montserrat", sans-serif; font-weight: 600; font-size: 30px; letter-spacing: 1px;
  }
  .back-arabic {
    font-family: "Noto Kufi Arabic", sans-serif; font-size: 13px; direction: rtl; margin-top: 2px; opacity: .95;
  }
</style>
</head>
<body>
<main class="stage">
  <section class="card card-front">
    <div class="brand-block">
      <span class="brand-dot"></span>
      <span class="brand-name">SABLE GRID</span>
    </div>
    <div class="divider"></div>
    <div class="contact-block">
      <p class="person-name">Faisal Alqurashi</p>
      <p class="person-title">General Manager</p>
      <ul class="contact-list">
        <li>
          <svg class="contact-icon" viewBox="0 0 14 14"><circle cx="7" cy="7" r="7" fill="var(--brand-blue)"/><path d="M4.5 3.8l1.4-.3.7 1.7-.9.6a5 5 0 0 0 2.5 2.5l.6-.9 1.7.7-.3 1.4c-3.4.2-5.9-2.3-5.7-5.7z" fill="#fff"/></svg>
          +966117290813
        </li>
        <li>
          <svg class="contact-icon" viewBox="0 0 14 14"><circle cx="7" cy="7" r="7" fill="var(--brand-blue)"/><rect x="5" y="3" width="4" height="8" rx="1" fill="#fff"/></svg>
          +9665031476095
        </li>
        <li>
          <svg class="contact-icon" viewBox="0 0 14 14"><circle cx="7" cy="7" r="7" fill="var(--brand-blue)"/><rect x="3.5" y="4.5" width="7" height="5" fill="#fff"/><path d="M3.5 4.5L7 7.3l3.5-2.8" stroke="var(--brand-blue)" stroke-width=".8" fill="none"/></svg>
          info@sablegrid.example
        </li>
        <li>
          <svg class="contact-icon" viewBox="0 0 14 14"><circle cx="7" cy="7" r="7" fill="var(--brand-blue)"/><circle cx="7" cy="7" r="3.5" fill="none" stroke="#fff" stroke-width=".9"/><path d="M3.5 7h7M7 3.5c-1.6 2-1.6 5 0 7M7 3.5c1.6 2 1.6 5 0 7" stroke="#fff" stroke-width=".7" fill="none"/></svg>
          www.sablegrid.example
        </li>
      </ul>
    </div>
  </section>

  <section class="card card-back">
    <div class="back-mark">
      <p class="back-name">SABLE GRID</p>
      <p class="back-arabic">شركة سابل جريد</p>
    </div>
  </section>
</main>
</body>
</html>
```